Real estate broker business card

Want a modern celan but effective business card for my residential and commercial real estate business. I want the back of the card to advertise my services and to capture business. I have attached the back of my current business card fore ideas
Updates

Target Market(s)

home buyers and seller. commercial buyers and sellers

Industry/Entity Type

Real Estate

Contact Information for Business Card

must have my contact information and my photo

Requirements
Must have
• Lorna Vettridge
• Owner & Qualifying Broker
• Brockhill Real Estate Services
• 555.218.7094
• lorna@brockhillhomes.example
• www.brockhillhomes.example
Nice to have
• metallic
• Business capture text: " Don't buy or lease property without someone looking out for your best interests. I will represent you on your home or investment purchase for FREE!"
• "Home owners, call today to receive a FREE market analysis for your homes value!

```html
<!DOCTYPE html>
<html lang="en">
<head>
<meta charset="utf-8">
<title>Brockhill Real Estate Services – Business Card</title>
<link rel="stylesheet" href="https://fonts.googleapis.com/css2?family=Montserrat:wght@500;700&family=Questrial&display=swap">
<style>
  :root {
    --stage-light: #d6d6d6;
    --stage-dark: #a9a9a9;
    --card-black: #050505;
    --card-charcoal: #1d1d1d;
    --teal: #1d8a9a;
    --white: #ffffff;
    --icon-hex: #4a4f55;
    --icon-blue: #2a9fd8;
    --photo-green: #2c4128;
    --photo-deep: #17231a;
  }
  * { margin: 0; padding: 0; box-sizing: border-box; }
  html, body { width: 1200px; height: 1200px; overflow: hidden; }
  body {
    position: relative;
    background: linear-gradient(90deg, var(--stage-dark), var(--stage-light) 50%, var(--stage-dark));
    font-family: "Questrial", "Century Gothic", sans-serif;
  }
  .card {
    position: absolute;
    left: 106px;
    width: 960px;
    height: 588px;
    overflow: hidden;
    box-shadow: 0 2px 6px rgba(0,0,0,.35);
  }
  .card--front {
    top: 4px;
    background: radial-gradient(ellipse at 75% 45%, var(--card-charcoal), var(--card-black) 70%);
  }
  .card--back { top: 604px; background: var(--card-black); }

  .brand { position: absolute; display: flex; align-items: center; }
  .brand__mark { border-radius: 50%; background: var(--teal); flex: none; }
  .brand__name {
    font-family: "Montserrat", sans-serif;
    font-weight: 500;
    color: var(--teal);
    text-transform: uppercase;
    line-height: 1;
  }
  .brand__name span { display: block; }

  .card--front .brand { left: 192px; top: 206px; gap: 26px; }
  .card--front .brand__mark { width: 150px; height: 150px; }
  .card--front .brand__word { font-size: 74px; letter-spacing: 2px; }
  .card--front .brand__sub { font-size: 24px; letter-spacing: 6.4px; margin-top: 14px; }

  .card--back .brand { left: 94px; top: 46px; gap: 18px; }
  .card--back .brand__mark { width: 106px; height: 106px; }
  .card--back .brand__word { font-size: 46px; letter-spacing: 1px; }
  .card--back .brand__sub { font-size: 15px; letter-spacing: 3.9px; margin-top: 9px; }

  .agent { position: absolute; left: 56px; top: 214px; color: var(--white); }
  .agent__name {
    font-family: "Montserrat", sans-serif;
    font-weight: 700;
    font-size: 35px;
    letter-spacing: .5px;
    text-transform: uppercase;
    padding: 0 4px 2px 4px;
    border-bottom: 1px solid var(--white);
  }
  .agent__title { font-size: 22px; margin: 5px 0 0 2px; }

  .contacts { position: absolute; left: 56px; top: 352px; list-style: none; color: var(--white); }
  .contacts li { display: flex; align-items: center; font-size: 26px; height: 40px; }
  .contacts li + li { margin-top: 31px; }
  .contacts li:last-child { margin-top: 17px; }
  .contacts svg { width: 32px; height: 34px; margin-right: 26px; flex: none; }

  .portrait {
    position: absolute;
    left: 518px;
    top: 0;
    width: 442px;
    height: 588px;
    background:
      linear-gradient(90deg, var(--card-black) 0%, rgba(5,5,5,0) 35%),
      radial-gradient(ellipse at 60% 55%, #6b5244 0%, #3a2a22 30%, transparent 55%),
      linear-gradient(160deg, var(--photo-green), var(--photo-deep));
  }
</style>
</head>
<body>
  <section class="card card--front">
    <div class="brand">
      <div class="brand__mark"></div>
      <div class="brand__name">
        <span class="brand__word">Brockhill</span>
        <span class="brand__sub">Real Estate Services</span>
      </div>
    </div>
  </section>

  <section class="card card--back">
    <div class="brand">
      <div class="brand__mark"></div>
      <div class="brand__name">
        <span class="brand__word">Brockhill</span>
        <span class="brand__sub">Real Estate Services</span>
      </div>
    </div>

    <div class="agent">
      <h1 class="agent__name">Lorna Vettridge</h1>
      <p class="agent__title">Owner &amp; Qualifying Broker</p>
    </div>

    <ul class="contacts">
      <li>
        <svg viewBox="0 0 32 34" aria-hidden="true">
          <polygon points="16,1 30,9 30,25 16,33 2,25 2,9" fill="var(--icon-hex)"/>
          <path d="M11 10c1-1 2-1 3 0l1.5 2.5c.5 1 0 1.7-.8 2.3.8 1.7 2 3 3.6 3.8.6-.8 1.3-1.3 2.3-.8L23 19.5c1 .8 1 1.8 0 2.8-1.6 1.6-4 1.4-6.8-.8-2.6-2-4.6-4.8-5.4-7.4-.5-1.8-.3-3.2.2-4.1z" fill="var(--icon-blue)"/>
        </svg>
        555.218.7094
      </li>
      <li>
        <svg viewBox="0 0 32 34" aria-hidden="true">
          <polygon points="16,1 30,9 30,25 16,33 2,25 2,9" fill="var(--icon-hex)"/>
          <rect x="8" y="11" width="16" height="12" fill="var(--icon-blue)"/>
          <path d="M8 11l8 7 8-7" fill="none" stroke="var(--icon-hex)" stroke-width="1.4"/>
        </svg>
        lorna@brockhillhomes.example
      </li>
      <li>
        <svg viewBox="0 0 32 34" aria-hidden="true">
          <polygon points="16,1 30,9 30,25 16,33 2,25 2,9" fill="var(--icon-hex)"/>
          <g fill="none" stroke="var(--icon-blue)" stroke-width="1.4">
            <circle cx="16" cy="17" r="7.5"/>
            <ellipse cx="16" cy="17" rx="3.2" ry="7.5"/>
            <path d="M8.5 17h15M10 13h12M10 21h12"/>
          </g>
        </svg>
        www.brockhillhomes.example
      </li>
    </ul>

    <div class="portrait" role="img" aria-label="Portrait photo of Lorna Vettridge against a leafy green background"></div>
  </section>
</body>
</html>
```